Cover of the e-book award-winning national sports figure.

I would like to utilize the picture this attached to this brief. If you could pull the trophies and myself out and place with the new background, that’s what I would like to see . I would like to have a new bookcover design for my e-book. I attached below the original cover and have marked in red. The things that I don’t want on the new cover. I’ve attached a picture that’s not the original. I’m waiting on the high copy. I would like to replace the old logo with the one that I have attached. The website that I would like to have on the book is www.dorianwmaxley.com.
Target Market(s)
Biography
Industry/Entity Type
Sports & motivation?
Requirements
Must have
- Picture of me in the blue suit on the cover the title of the book carving out the path diary of a steady runner
Nice to have
- Utilize the old cover that I have attached for some ideas
Should not have
- The cover should not have anything related to brightvale books Inc.

```html
<!DOCTYPE html>
<html lang="en">
<head>
<meta charset="utf-8">
<title>Carving Out the Path – Book Cover</title>
<link rel="stylesheet" href="https://fonts.googleapis.com/css2?family=Anton&family=Cinzel:wght@400;500&family=Oswald:wght@500&family=Great+Vibes&family=Courier+Prime:wght@700&family=Tinos&display=swap">
<style>
  :root {
    --page: #ffffff;
    --cream: #f3f0e8;
    --cover-blue: #3b5a9e;
    --spine-blue: #3a5798;
    --photo-blue: #2f6cae;
    --photo-deep: #1d3f74;
    --mist-light: #f2f1ec;
    --mist-mid: #c9c7c0;
    --ink: #1e1e1e;
    --navy: #233a6b;
    --white: #ffffff;
    --outline: #1a1a1a;
  }
  html, body { margin: 0; padding: 0; overflow: hidden; }
  body { width: 1200px; height: 1200px; background: var(--page); position: relative; }

  .cover { position: absolute; top: 288px; height: 618px; overflow: hidden; }

  /* Back cover */
  .back-cover { left: 89px; width: 423px; background: var(--cream); }
  .back-photo {
    position: absolute; inset: 0;
    background: linear-gradient(160deg, var(--photo-blue) 0%, #3d82c4 40%, var(--photo-deep) 100%);
    clip-path: polygon(155px 0, 423px 0, 423px 618px, 107px 618px);
  }
  .back-brand {
    position: absolute; left: 14px; top: 58px; width: 150px;
    display: flex; align-items: center; gap: 6px;
    font-family: "Oswald", sans-serif; font-weight: 500; font-size: 13px;
    color: var(--ink); letter-spacing: 0.5px;
  }
  .brand-dot { width: 12px; height: 12px; border-radius: 50%; background: var(--photo-blue); flex: none; }
  .about-heading {
    position: absolute; left: 158px; top: 116px; margin: 0;
    font-family: "Cinzel", serif; font-weight: 400; font-size: 15px; line-height: 18px;
    color: var(--white);
  }
  .intro-panel {
    position: absolute; left: 37px; top: 192px; width: 355px; height: 324px;
    background: rgba(255,255,255,0.55); box-sizing: border-box; padding: 9px 12px 0 39px;
  }
  .intro-panel h3 {
    margin: 0 0 14px; font-family: "Oswald", sans-serif; font-weight: 500;
    font-size: 11.5px; color: var(--ink); letter-spacing: 0.2px;
  }
  .intro-panel p {
    margin: 0; font-family: "Tinos", serif; font-size: 10.6px; line-height: 14.8px;
    color: #2a2a2a; text-align: justify;
  }

  /* Spine */
  .spine { left: 563px; width: 71px; background: var(--spine-blue); }
  .spine-text {
    position: absolute; left: 50%; transform: translateX(-50%);
    writing-mode: vertical-rl; color: var(--white); white-space: nowrap;
  }
  .spine-author { top: 30px; font-family: "Cinzel", serif; font-size: 30px; font-weight: 500; }
  .spine-subtitle { top: 225px; font-family: "Great Vibes", cursive; font-size: 22px; line-height: 24px; white-space: normal; height: 110px; }
  .spine-title { bottom: 32px; font-family: "Cinzel", serif; font-size: 16px; }

  /* Front cover */
  .front-cover { left: 676px; width: 422px; background: var(--cover-blue); }
  .front-mist {
    position: absolute; inset: 0;
    background: linear-gradient(200deg, #a9a7a1 0%, var(--mist-mid) 25%, var(--mist-light) 60%, var(--mist-light) 100%);
    clip-path: polygon(252px 0, 422px 0, 422px 618px, 304px 618px);
  }
  .portrait {
    position: absolute; left: 228px; top: 150px; width: 100px; height: 440px; z-index: 1;
    border-radius: 46px 46px 10px 10px;
    background: linear-gradient(180deg, #d9c77a 0%, #e8dc8f 35%, #2a2a2a 60%, #1b1b1b 92%, #f0f0f0 100%);
  }
  .front-title {
    position: absolute; left: 18px; top: 22px; margin: 0; z-index: 2;
    font-family: "Anton", sans-serif; font-weight: 400; font-size: 104px; line-height: 131px;
    color: var(--white); -webkit-text-stroke: 2px var(--outline); letter-spacing: 1px;
    text-transform: uppercase;
  }
  .front-title span { display: block; }
  .front-author {
    position: absolute; left: 30px; top: 440px; margin: 0; z-index: 2;
    font-family: "Cinzel", serif; font-weight: 400; font-size: 40px; line-height: 48px;
    color: var(--white);
  }
  .front-subtitle {
    position: absolute; left: 14px; top: 566px; z-index: 2;
    font-family: "Great Vibes", cursive; font-size: 23px; color: var(--white); white-space: nowrap;
  }
  .front-brand {
    position: absolute; left: 336px; top: 448px; width: 82px; z-index: 2;
    display: flex; align-items: center; gap: 4px;
    font-family: "Oswald", sans-serif; font-weight: 500; font-size: 9px; color: var(--ink); white-space: nowrap;
  }
  .front-brand .brand-dot { width: 8px; height: 8px; }
  .foreword {
    position: absolute; left: 318px; top: 580px; margin: 0; z-index: 2;
    font-family: "Courier Prime", monospace; font-weight: 700; font-size: 12px; line-height: 14px;
    color: var(--navy);
  }
</style>
</head>
<body>
  <section class="cover back-cover">
    <div class="back-photo" role="img" aria-label="Photo of the author in a blue pinstripe suit standing beside trophies"></div>
    <div class="back-brand"><span class="brand-dot"></span>DORIAN MAXLEY</div>
    <h2 class="about-heading">ABOUT<br>DORIAN<br>MAXLEY</h2>
    <div class="intro-panel">
      <h3>FROM DORIAN MAXLEY'S INTRODUCTION</h3>
      <p>Becoming a team player is absolutely crucial to your ultimate success. Learning to play within the framework of a team atmosphere not only strengthens your individual ability, but it also gives you a tremendous feeling of accomplishment knowing that you've been instrumental in moving an entire group of people a little closer to the collective dream. I believe that the personal and professional experiences shared in this book will offer strategies that can be used in any team situation, whether its a corporate sales force, a little league sports team, a social organization or a family unit</p>
    </div>
  </section>

  <section class="cover spine">
    <div class="spine-text spine-author">MAXLEY</div>
    <div class="spine-text spine-subtitle">Diary of a Steady Runner</div>
    <div class="spine-text spine-title">CARVING OUT THE PATH</div>
  </section>

  <section class="cover front-cover">
    <div class="front-mist"></div>
    <div class="portrait" role="img" aria-label="Photo of the author holding championship trophies"></div>
    <h1 class="front-title"><span>Carving</span><span>Out the</span><span>Path</span></h1>
    <h2 class="front-author">DORIAN<br>MAXLEY</h2>
    <div class="front-subtitle">Diary of a Steady Runner</div>
    <div class="front-brand"><span class="brand-dot"></span>DORIAN MAXLEY</div>
    <p class="foreword">Foreword by<br>Marcus Ellery</p>
  </section>
</body>
</html>
```